Recovery Lounge

We are opening a recovering lounge in our physical therapy clinic. We would like a menu of our services that we can offer guest. We would like it to flow well with our brand. Ive attached a doc of our prices an basic idea of what we are looking for.

our website is lumoraptclinic.com if your need brand inspiration.

```html
<!DOCTYPE html>
<html lang="en">
<head>
<meta charset="utf-8">
<title>Lumora Recovery Lounge Menu</title>
<link rel="stylesheet" href="https://fonts.googleapis.com/css2?family=Great+Vibes&family=Pinyon+Script&family=Cormorant+Garamond:wght@500;700&family=Source+Sans+3:ital,wght@0,400;0,700;1,400;1,700&family=Poppins:ital,wght@0,400;0,600;1,400&display=swap">
<style>
  :root {
    --backdrop: #a19fac;
    --paper: #fdf9f7;
    --purple: #3e2b8e;
    --coral: #e8684a;
    --ink: #2a2a2a;
    --rule: #3b4740;
    --cream: #faf0de;
    --gold-rule: #d6bf8d;
  }
  * { box-sizing: border-box; margin: 0; padding: 0; }
  html, body { width: 970px; height: 1200px; overflow: hidden; background: var(--backdrop); }
  .canvas { position: relative; width: 970px; height: 1200px; background: var(--backdrop); }
  .menu { position: absolute; left: 70px; top: 66px; width: 831px; height: 1068px; background: var(--paper); }

  .brand { position: absolute; top: 42px; left: 0; width: 100%; display: flex; justify-content: center; align-items: center; gap: 14px; }
  .brand-dot { width: 34px; height: 34px; border-radius: 50%; background: var(--coral); }
  .brand-name { font-family: "Poppins", sans-serif; font-weight: 600; font-size: 50px; line-height: 1; color: var(--purple); letter-spacing: 0.5px; }

  .title { position: absolute; top: 100px; left: 0; width: 100%; text-align: center; font-family: "Great Vibes", cursive; font-size: 100px; line-height: 1.2; color: var(--purple); }

  .section-head { position: absolute; display: flex; align-items: center; gap: 14px; }
  .section-head .line { flex: 1; height: 1.2px; background: var(--purple); }
  .section-head h2 { font-family: "Cormorant Garamond", serif; font-weight: 500; color: var(--coral); white-space: nowrap; line-height: 1; }
  .alacarte-head { left: 114px; top: 306px; width: 580px; }
  .alacarte-head h2 { font-size: 46px; }
  .bundles-head { left: 62px; top: 614px; width: 715px; }
  .bundles-head h2 { font-size: 50px; }
  .bundles-head h2 strong { font-weight: 700; font-size: 56px; }

  .price-list { position: absolute; left: 114px; top: 363px; width: 588px; list-style: none; }
  .price-row { position: relative; height: 47px; display: flex; align-items: center; font-family: "Source Sans 3", sans-serif; font-size: 21px; color: var(--ink); border-bottom: 1.2px solid var(--rule); }
  .price-row:last-child { border-bottom: none; }
  .price-row .service { position: absolute; left: 37px; }
  .price-row .duration { position: absolute; left: 394px; font-style: italic; }
  .price-row .price { position: absolute; left: 587px; transform: translateX(-100%); font-weight: 700; color: var(--purple); }
  .price-row .price { left: 525px; transform: none; }

  .bundles { position: absolute; left: 63px; top: 611px; width: 715px; height: 374px; background: var(--cream); }
  .bundle { position: absolute; left: 49px; width: 635px; height: 90px; }
  .bundle + .bundle { border-top: 1.2px solid var(--gold-rule); }
  .bundle-title { position: absolute; left: 0; display: flex; align-items: baseline; white-space: nowrap; color: var(--purple); }
  .bundle-name { font-family: "Pinyon Script", cursive; font-size: 40px; line-height: 1; margin-right: 8px; }
  .bundle-meta { font-family: "Poppins", sans-serif; font-size: 20px; }
  .bundle-meta strong { font-weight: 600; }
  .bundle-items { position: absolute; left: 0; font-family: "Poppins", sans-serif; font-style: italic; font-size: 12.5px; color: var(--ink); }
  .bundle-save { position: absolute; left: 528px; font-family: "Poppins", sans-serif; font-size: 19px; color: var(--coral); }

  .note { position: absolute; left: 0; top: 1005px; width: 100%; text-align: center; font-family: "Source Sans 3", sans-serif; font-style: italic; font-weight: 700; font-size: 17px; color: var(--ink); letter-spacing: -0.3px; }
  .note em { color: var(--purple); }
</style>
</head>
<body>
<div class="canvas">
  <main class="menu">
    <header class="brand">
      <span class="brand-dot"></span>
      <span class="brand-name">lumora</span>
    </header>
    <h1 class="title">Recovery Lounge</h1>

    <div class="section-head alacarte-head"><span class="line"></span><h2>A la carte</h2><span class="line"></span></div>
    <ul class="price-list">
      <li class="price-row"><span class="service">Infrared Sauna + Red Light</span><span class="duration">(30 min)</span><span class="price">$40</span></li>
      <li class="price-row"><span class="service">Infrared Sauna + Red Light</span><span class="duration">(60 min)</span><span class="price">$65</span></li>
      <li class="price-row"><span class="service">Flowtec Compression</span><span class="duration">(30 min)</span><span class="price">$40</span></li>
      <li class="price-row"><span class="service">Flowtec Compression</span><span class="duration">(60 min)</span><span class="price">$65</span></li>
      <li class="price-row"><span class="service">Paraffin Hand Bath</span><span class="duration">(15 min)</span><span class="price">$25</span></li>
    </ul>

    <div class="section-head bundles-head"><span class="line"></span><h2><strong>Bundles</strong> (best sellers)</h2><span class="line"></span></div>
    <section class="bundles">
      <div class="bundle" style="top:8px;">
        <div class="bundle-title" style="top:28px;"><span class="bundle-name">Reset</span><span class="bundle-meta">(45 min) – <strong>$55</strong></span></div>
        <div class="bundle-items" style="top:64px;">Choose 1: Sauna (30) or Flowtec (30) + Paraffin</div>
        <div class="bundle-save" style="top:36px;">(Save $10)</div>
      </div>
      <div class="bundle" style="top:161px; height:90px;">
        <div class="bundle-title" style="top:22px;"><span class="bundle-name">Refresh</span><span class="bundle-meta">(60 min) – <strong>$65</strong></span></div>
        <div class="bundle-items" style="top:64px;">Sauna (30) + Flowtec (30)</div>
        <div class="bundle-save" style="top:24px;">(Save $15)</div>
      </div>
      <div class="bundle" style="top:251px; height:92px;">
        <div class="bundle-title" style="top:18px;"><span class="bundle-name">Restore</span><span class="bundle-meta">(75 min) – <strong>$85</strong></span></div>
        <div class="bundle-items" style="top:60px;">Sauna (30) + Flowtec (30) + Paraffin</div>
        <div class="bundle-save" style="top:22px;">(Save $20)</div>
      </div>
      <div class="bundle" style="top:343px; height:30px; border-top:none;"></div>
      <div class="bundle" style="top:343px; height:0;">
        <div class="bundle-title" style="top:22px;"><span class="bundle-name">Rejuvenate</span><span class="bundle-meta">(135 min) – <strong>$130</strong></span></div>
      </div>
    </section>
    <div style="position:absolute; left:112px; top:1035px;"></div>
    <p class="note">*For safety, a rest/cool-down period is required after <em>30 minutes in the sauna.</em></p>
  </main>
</div>
<style>
  /* Rejuvenate sits in the last band of the bundles panel */
  .bundles { overflow: visible; }
  .bundle:nth-child(5) { top: 343px !important; border-top: 1.2px solid var(--gold-rule); width: 635px; }
  .bundle:nth-child(5) .bundle-title { top: 8px !important; }
  .bundle:nth-child(4) { display: none; }
  .bundle:nth-child(5)::after { content: "Sauna (60) + Flowtec (60) + Paraffin"; position: absolute; left: 0; top: 58px; font-family: "Poppins", sans-serif; font-style: italic; font-size: 12.5px; color: var(--ink); white-space: nowrap; }
  .bundle:nth-child(5)::before { content: "(Save $25)"; position: absolute; left: 528px; top: 16px; font-family: "Poppins", sans-serif; font-size: 19px; color: var(--coral); }
  .bundles { height: 374px; }
  .bundle:nth-child(2) { top: 161px !important; }
  .bundle:nth-child(3) { top: 251px !important; }
  .bundle:nth-child(5) { top: 343px !important; }
  .bundle:nth-child(1) { top: 8px; }
  .bundle:nth-child(2) { top: 94px !important; }
  .bundle:nth-child(3) { top: 184px !important; }
  .bundle:nth-child(5) { top: 276px !important; }
</style>
</body>
</html>
```